Flyer-Design für Personalvermittlung
Zielgruppe
Wir machen Personalvermittlung (www.kraftwendel.de), Unternehmen, die einen eigenen Kunden haben sowie Unternehmen, die Kundenservice als Dienstleistung anbieten. DIe Zielgruppe sind Personalentscheider, Recruiter, HR-Direktoren, Kundenservicecenter-Leiter, Geschäftsführer). Weiterhin zählt zur Zielgruppe jeder wechselwillige Kandidat, der sich bei kraftwendel registrieren kann.
Aufgabenstellung
Ich hätte gerne ein zweiseitiges Flyerformat, was über Hostessen verteilbar ist, also nicht größer als A5. Inhalte können gerne aus der Homepage entnommen werden. Weiterhin in der Anlage ein Teaser, den wir Unternehmen zur Verfügung stellen. Vorderseite für Unternehmen, Rückseite für Kandidaten. Kernige Aussagen, wenig Text.

```html
<!DOCTYPE html>
<html lang="de">
<head>
<meta charset="utf-8">
<title>kraftwendel Flyer – Vorder- und Rückseite</title>
<link href="https://fonts.googleapis.com/css2?family=Roboto+Condensed:ital,wght@0,300;0,400;0,700;1,300&family=Montserrat:wght@700;800&display=swap" rel="stylesheet">
<style>
  :root{
    --teal:#3bb291;
    --ink:#111a1a;
    --text:#1d1d1d;
    --paper:#ffffff;
    --stage:#ececec;
  }
  *{box-sizing:border-box;margin:0;padding:0}
  html,body{width:849px;height:1200px;overflow:hidden;background:var(--stage)}
  body{position:relative;font-family:"Roboto Condensed",Arial,sans-serif;color:var(--text)}

  .flyer{position:absolute;top:195px;width:405px;height:810px;background:var(--paper);
    box-shadow:0 2px 8px rgba(0,0,0,.18);overflow:hidden}
  .flyer--front{left:13px}
  .flyer--back{left:431px}

  .header-band{position:absolute;left:0;top:0;width:100%;background:var(--teal);
    display:flex;align-items:center;justify-content:center;text-align:center;
    font-weight:300;font-size:15px;line-height:1.35;color:var(--ink);padding:0 18px}
  .flyer--front .header-band{height:74px}
  .flyer--back .header-band{height:54px;font-size:16px}
  .header-band b{font-family:"Montserrat",Arial,sans-serif;font-weight:800;font-size:.93em}

  .quote{position:absolute;left:14px;right:18px;display:flex;gap:10px}
  .flyer--front .quote{top:109px}
  .flyer--back .quote{top:88px}
  .quote-mark{flex:0 0 44px;height:48px;background:var(--teal)}
  .quote-body{flex:1}
  .quote-text{font-style:italic;font-weight:300;font-size:10px;line-height:1.5}
  .quote-author{text-align:right;font-style:italic;font-weight:300;font-size:7.5px;margin-top:3px}

  .photo{position:absolute;left:19px;width:367px}
  .photo--office{top:187px;height:251px;
    background:linear-gradient(135deg,#f4f1ec 0%,#d9cdbd 45%,#9f8a74 75%,#c9c3b8 100%);
    clip-path:polygon(0 0,95% 0,100% 6%,100% 100%,11% 100%,0 87%)}
  .photo--team{top:168px;height:251px;
    background:linear-gradient(120deg,#c69a72 0%,#7a6656 30%,#3f4a5c 55%,#c9a27e 80%,#e3ddd5 100%);
    clip-path:polygon(0 0,96% 0,100% 5%,100% 100%,11% 100%,0 88%)}

  .features{position:absolute;top:0;bottom:0;left:17px;right:18px;list-style:none}
  .feature{position:absolute;left:0;right:0;display:flex;gap:8px}
  .feature-icon{flex:0 0 48px;width:48px;height:48px}
  .feature-copy{flex:1}
  .feature-title{display:flex;align-items:center;gap:4px;font-weight:400;font-size:13px;color:var(--ink);line-height:1.1}
  .feature-title svg{width:10px;height:10px}
  .feature-text{font-weight:300;font-size:9.6px;line-height:1.5;margin-top:2px}
  .flyer--back .feature-text{text-align:justify}
  .feature-text b{font-weight:700}

  .footer-band{position:absolute;left:0;bottom:0;width:100%;height:48px;background:var(--teal);
    display:flex;align-items:center;justify-content:center;padding-left:26px}
  .site-url{font-family:"Montserrat",Arial,sans-serif;font-weight:800;font-size:19px;color:var(--ink)}
  .brand-dot{position:absolute;left:20px;bottom:24px;width:49px;height:49px;border-radius:50%;background:var(--ink)}
</style>
</head>
<body>

<svg width="0" height="0" style="position:absolute" aria-hidden="true">
  <defs>
    <symbol id="bullet-arrow" viewBox="0 0 10 10">
      <circle cx="5" cy="5" r="5" fill="#3bb291"/>
      <path d="M2.5 5h4M5 3l2 2-2 2" stroke="#fff" stroke-width="1.3" fill="none" stroke-linecap="round"/>
    </symbol>
  </defs>
</svg>

<!-- Vorderseite: Unternehmen -->
<section class="flyer flyer--front">
  <header class="header-band">
    <p>Finden Sie die <b>besten Mitarbeiter</b> für Ihre Aufgaben im <b>Kundenservice</b> und im <b>Call Center</b>.</p>
  </header>

  <div class="quote">
    <div class="quote-mark"></div>
    <div class="quote-body">
      <p class="quote-text">Durch den klaren Fokus auf diese Branche haben Unternehmen mit kraftwendel deutschlandweit Zugriff auf wechselwillige oder sofort verfügbare Agenten, Kundenbetreuer, Spezialisten und Führungskräfte.</p>
      <p class="quote-author">– Lars Brennecke –</p>
    </div>
  </div>

  <div class="photo photo--office" role="img" aria-label="Foto: Mitarbeiterin mit Headset am Arbeitsplatz in einem hellen Call-Center-Büro"></div>

  <ul class="features">
    <li class="feature" style="top:466px">
      <svg class="feature-icon" viewBox="0 0 49 49" aria-hidden="true">
        <circle cx="24.5" cy="24.5" r="24.5" fill="#111a1a"/>
        <circle cx="24.5" cy="24.5" r="12" fill="#3bb291"/>
        <text x="24.5" y="30" text-anchor="middle" font-family="Arial" font-weight="700" font-size="15" fill="#111a1a">€</text>
      </svg>
      <div class="feature-copy">
        <h3 class="feature-title"><svg><use href="#bullet-arrow"/></svg>Günstig</h3>
        <p class="feature-text">kraftwendel ist bis zu <b>50 % günstiger</b> als die klassischen Headhunter und Personalvermittler.</p>
      </div>
    </li>
    <li class="feature" style="top:558px">
      <svg class="feature-icon" viewBox="0 0 49 49" aria-hidden="true">
        <circle cx="24.5" cy="24.5" r="24.5" fill="#111a1a"/>
        <path d="M24.5 11l11 4v8c0 8-5 13-11 15-6-2-11-7-11-15v-8z" fill="#3bb291"/>
        <path d="M19.5 24.5l3.5 3.5 6.5-7" stroke="#111a1a" stroke-width="2" fill="none" stroke-linecap="round"/>
      </svg>
      <div class="feature-copy">
        <h3 class="feature-title"><svg><use href="#bullet-arrow"/></svg>Risikolos</h3>
        <p class="feature-text">kraftwendel bietet Ihnen ein <b>erfolgsbasiertes Honorarmodell</b>.</p>
      </div>
    </li>
    <li class="feature" style="top:634px">
      <svg class="feature-icon" viewBox="0 0 49 49" aria-hidden="true">
        <circle cx="24.5" cy="24.5" r="24.5" fill="#111a1a"/>
        <rect x="14" y="17" width="19" height="17" rx="1.5" fill="#3bb291"/>
        <circle cx="23.5" cy="16" r="4" fill="#3bb291"/>
        <circle cx="34" cy="25.5" r="4" fill="#3bb291"/>
        <circle cx="14" cy="25.5" r="3" fill="#111a1a"/>
      </svg>
      <div class="feature-copy">
        <h3 class="feature-title"><svg><use href="#bullet-arrow"/></svg>Passend</h3>
        <p class="feature-text">Durch unseren Pairing-Algorithmus oder durch Active Sourcing erhalten Sie von uns <b>passende Kandidaten</b> auf Ihre Stellenausschreibung – vom Kundenbetreuer bis zum CEO.</p>
      </div>
    </li>
  </ul>

  <footer class="footer-band"><span class="site-url">www.kraftwendel.de</span></footer>
  <div class="brand-dot"></div>
</section>

<!-- Rückseite: Kandidaten -->
<section class="flyer flyer--back">
  <header class="header-band">
    <p>Wir finden den <b>richtigen Job</b> für <b>Ihre Karriere!</b></p>
  </header>

  <div class="quote">
    <div class="quote-mark"></div>
    <div class="quote-body">
      <p class="quote-text">Es gibt viele Jobportale, aber keines, welches sich ausschließlich auf die Anforderungen und Wünsche von Mitarbeitern im Umfeld des Kundenservice und Call Centers fokussiert.</p>
      <p class="quote-author">– Lars Brennecke –</p>
    </div>
  </div>

  <div class="photo photo--team" role="img" aria-label="Fotoraster: sechs Porträts lächelnder junger Fachkräfte"></div>

  <ul class="features">
    <li class="feature" style="top:445px">
      <svg class="feature-icon" viewBox="0 0 49 49" aria-hidden="true">
        <circle cx="24.5" cy="24.5" r="24.5" fill="#111a1a"/>
        <circle cx="24.5" cy="21" r="7" fill="#3bb291"/>
        <path d="M13 36c2-6 6-8 11.5-8s9.5 2 11.5 8z" fill="#3bb291"/>
        <path d="M16 21a8.5 8.5 0 0 1 17 0" stroke="#3bb291" stroke-width="2" fill="none"/>
        <path d="M33 22v3c0 2-2 3-5 3" stroke="#3bb291" stroke-width="1.6" fill="none"/>
      </svg>
      <div class="feature-copy">
        <h3 class="feature-title"><svg><use href="#bullet-arrow"/></svg>Für Agenten</h3>
        <p class="feature-text">Sie sind Berufseinsteiger oder haben bereits Berufserfahrung im Kundenservice? Als Kundenbetreuer oder Agent im Kundenservice macht Ihnen keiner etwas vor? Dann melden Sie sich hier an und finden Sie Ihre berufliche Herausforderung!</p>
      </div>
    </li>
    <li class="feature" style="top:537px">
      <svg class="feature-icon" viewBox="0 0 49 49" aria-hidden="true">
        <circle cx="24.5" cy="24.5" r="24.5" fill="#111a1a"/>
        <circle cx="24.5" cy="17" r="4" fill="#3bb291"/>
        <path d="M19 33v-7c0-3 2.5-4.5 5.5-4.5s5.5 1.5 5.5 4.5v7z" fill="#3bb291"/>
        <circle cx="15" cy="22" r="3" fill="#3bb291"/>
        <path d="M10.5 34v-5c0-2.5 2-3.5 4.5-3.5s4 1 4 3.5v5z" fill="#3bb291"/>
        <circle cx="34" cy="22" r="3" fill="#3bb291"/>
        <path d="M30 34v-5c0-2.5 1.5-3.5 4-3.5s4.5 1 4.5 3.5v5z" fill="#3bb291"/>
      </svg>
      <div class="feature-copy">
        <h3 class="feature-title"><svg><use href="#bullet-arrow"/></svg>Für Spezialisten</h3>
        <p class="feature-text">Sie kennen die operativen Abläufe im Kundenservice? Ihre Erfahrungen kommen aus dem WFM (Workforce Management), der Personaleinsatzplanung, dem Bereich Personal, der Buchhaltung, der IT oder dem Training?<br>Wir finden für Sie eine neue berufliche Perspektive!</p>
      </div>
    </li>
    <li class="feature" style="top:642px">
      <svg class="feature-icon" viewBox="0 0 49 49" aria-hidden="true">
        <circle cx="24.5" cy="24.5" r="24.5" fill="#111a1a"/>
        <circle cx="24.5" cy="18" r="6.5" fill="#3bb291"/>
        <path d="M13 36c1-6 5-9 11.5-9s10.5 3 11.5 9z" fill="#3bb291"/>
        <path d="M24.5 27l-2 3 2 6 2-6z" fill="#111a1a"/>
      </svg>
      <div class="feature-copy">
        <h3 class="feature-title"><svg><use href="#bullet-arrow"/></svg>Für Führungskräfte</h3>
        <p class="feature-text">Sie haben bereits Führungserfahrung oder Sie suchen den nächsten Schritt als Team-, Projekt- oder Standortleiter, als Key Account Manager oder als Leiter einer Fachabteilung im Kundenservice? Dann sind Sie hier genau richtig!</p>
      </div>
    </li>
  </ul>

  <footer class="footer-band"><span class="site-url">www.kraftwendel.de</span></footer>
  <div class="brand-dot"></div>
</section>

</body>
</html>
```